Real Estate Business Cards

Looking for a clean, sharp and professional look for our Real Estate investment Fund that invests in Multi Family Apartment buildings.

Target Market(s)

Real Estate Fund

Industry/Entity Type

Real Estate

Contact Information for Business Card

Company Description: Real Estate Investment Fund
Company Name: RKW Holdings
Name: Marcus Olvane
Cell: (917) 482-0657
Email: marcus@rkwholdings-example.com
Website: www.rkwholdings-example.com
Address: 418, 9th Street, Brooklyn NY 11218

Colors

Designer to choose colors to be used in the design.

Requirements
Nice to have
• Colors to match logo

```html
<!DOCTYPE html>
<html lang="en">
<head>
<meta charset="utf-8">
<title>RKW Holdings – Business Card</title>
<link href="https://fonts.googleapis.com/css2?family=Questrial&family=Didact+Gothic&display=swap" rel="stylesheet">
<style>
  :root {
    --backdrop: #a5a5a5;
    --card: #ffffff;
    --brand-blue: #3e6fae;
    --ink: #1f1f24;
    --ink-soft: #2b2b2b;
  }
  * { margin: 0; padding: 0; box-sizing: border-box; }
  html, body { width: 1200px; height: 1200px; overflow: hidden; }
  body { background: var(--backdrop); position: relative; font-family: "Questrial", sans-serif; }

  .card {
    position: absolute;
    left: 258px;
    width: 678px;
    height: 376px;
    background: var(--card);
  }
  .card--front { top: 224px; }
  .card--back { top: 632px; }

  .brand-mark {
    position: absolute;
    background: var(--brand-blue);
  }
  .card--front .brand-mark { left: 199px; top: 160px; width: 42px; height: 42px; }
  .brand-name {
    position: absolute;
    font-family: "Questrial", sans-serif;
    color: var(--brand-blue);
    text-transform: uppercase;
    white-space: nowrap;
  }
  .card--front .brand-name {
    left: 160px; top: 214px; width: 120px;
    text-align: center; font-size: 11px; letter-spacing: 1.5px;
  }

  .holder-name {
    position: absolute;
    left: 302px; top: 134px;
    font-family: "Questrial", sans-serif;
    font-weight: 400;
    font-size: 31px;
    color: var(--ink);
    -webkit-text-stroke: 0.6px var(--ink);
    letter-spacing: 0.2px;
  }
  .contact-rule {
    position: absolute;
    left: 303px; top: 178px;
    width: 1.5px; height: 70px;
    background: var(--brand-blue);
  }
  .contact-list { list-style: none; position: absolute; left: 324px; top: 175px; }
  .contact-item {
    display: flex; align-items: center;
    height: 19.5px;
    font-family: "Didact Gothic", sans-serif;
    font-size: 10.5px;
    letter-spacing: 1.1px;
    color: var(--ink-soft);
  }
  .contact-icon { width: 13px; height: 13px; margin-right: 8px; fill: var(--brand-blue); flex: none; }

  .card--back .brand-mark { left: 216px; top: 176px; width: 26px; height: 26px; }
  .card--back .brand-name {
    left: 256px; top: 174px;
    font-size: 27px; letter-spacing: 2px; line-height: 30px;
  }
</style>
</head>
<body>
  <section class="card card--front">
    <div class="brand-mark"></div>
    <div class="brand-name">RKW Holdings</div>
    <h1 class="holder-name">Marcus Olvane</h1>
    <div class="contact-rule"></div>
    <ul class="contact-list">
      <li class="contact-item">
        <svg class="contact-icon" viewBox="0 0 24 24"><path d="M6.6 10.8a15.5 15.5 0 0 0 6.6 6.6l2.2-2.2c.3-.3.7-.4 1-.2 1.1.4 2.3.6 3.6.6.6 0 1 .4 1 1V20c0 .6-.4 1-1 1A17 17 0 0 1 3 4c0-.6.4-1 1-1h3.5c.6 0 1 .4 1 1 0 1.3.2 2.5.6 3.6.1.3 0 .7-.2 1z"/></svg>
        (917) 482-0657
      </li>
      <li class="contact-item">
        <svg class="contact-icon" viewBox="0 0 24 24"><path d="M2 5h20v14H2z" fill="var(--brand-blue)"/><path d="M2 5l10 8 10-8" fill="none" stroke="#fff" stroke-width="1.8"/></svg>
        marcus@rkwholdings-example.com
      </li>
      <li class="contact-item">
        <svg class="contact-icon" viewBox="0 0 24 24"><g fill="none" stroke="var(--brand-blue)" stroke-width="1.6"><circle cx="12" cy="12" r="9.5"/><ellipse cx="12" cy="12" rx="4" ry="9.5"/><path d="M2.5 12h19M4 7h16M4 17h16"/></g></svg>
        www.rkwholdings-example.com
      </li>
      <li class="contact-item">
        <svg class="contact-icon" viewBox="0 0 24 24"><path d="M12 2a7 7 0 0 0-7 7c0 5.2 7 13 7 13s7-7.8 7-13a7 7 0 0 0-7-7zm0 9.5A2.5 2.5 0 1 1 12 6.5a2.5 2.5 0 0 1 0 5z"/></svg>
        418, 9th Street, Brooklyn NY 11218
      </li>
    </ul>
  </section>

  <section class="card card--back">
    <div class="brand-mark"></div>
    <div class="brand-name">RKW Holdings</div>
  </section>
</body>
</html>
```